Need Responsive Email Newsletter Design

Looking for a clean, professional newsletter to send in our next email blast to our customers. Need a combination Graduation Gift and Father's Day theme for our briefcases and travel bags. "40% - 75% Off Storewide!" "Free Shipping On All Orders (No Minimum Required)!" "Make it extra special with a custom monogram!" Some sample photos are attached. Please, only top quality designers apply!
Updates
Logo and company can be found at Satchelry.com. Added Friday, May 8, 2015
Industry/Entity Type
It Professional
Look and feel
Each slider illustrates characteristics of the customer's brand and the style your logo design should communicate.

```html
<!DOCTYPE html>
<html lang="en">
<head>
<meta charset="utf-8">
<title>Graduation Gift &amp; Father's Day Sale 2015</title>
<link rel="stylesheet" href="https://fonts.googleapis.com/css2?family=Montserrat:ital,wght@0,300;0,400;0,700;1,300&display=swap">
<style>
  :root {
    --ink: #000000;
    --paper: #ffffff;
    --leather-red: #7a2e12;
    --leather-red-light: #a4471d;
    --leather-tan: #7d4a2a;
    --leather-tan-light: #a06a44;
    --shadow: rgba(0, 0, 0, 0.35);
  }
  * { margin: 0; padding: 0; box-sizing: border-box; }
  html, body {
    width: 1200px;
    height: 900px;
    overflow: hidden;
    background: var(--paper);
  }
  .newsletter {
    position: relative;
    width: 1200px;
    height: 900px;
    font-family: "Montserrat", Arial, sans-serif;
    color: var(--paper);
  }
  .occasion-bar {
    position: absolute;
    left: 22px;
    top: 29px;
    width: 1162px;
    height: 70px;
    filter: drop-shadow(0 2px 3px var(--shadow));
  }
  .occasion-bar svg { display: block; }
  .occasion-label {
    position: absolute;
    top: 0;
    height: 70px;
    line-height: 70px;
    font-size: 15px;
    font-weight: 700;
    letter-spacing: 0.2px;
    text-transform: uppercase;
  }
  .occasion-label.graduation { left: 19px; }
  .occasion-label.fathers-day { left: 353px; }
  .occasion-year {
    position: absolute;
    right: 19px;
    top: 0;
    height: 70px;
    line-height: 70px;
    font-size: 15px;
    font-weight: 300;
  }
  .product-stage {
    position: absolute;
    left: 22px;
    top: 123px;
    width: 1162px;
    height: 332px;
  }
  .product-stage svg {
    display: block;
    filter: drop-shadow(0 1px 4px var(--shadow));
  }
  .product-photo {
    position: absolute;
    border-radius: 18px;
  }
  .product-photo.backpack {
    left: 60px;
    top: 36px;
    width: 235px;
    height: 252px;
    background: radial-gradient(ellipse at 45% 40%, var(--leather-red-light), var(--leather-red) 70%);
  }
  .product-photo.briefcase {
    left: 835px;
    top: 42px;
    width: 265px;
    height: 236px;
    background: radial-gradient(ellipse at 45% 40%, var(--leather-tan-light), var(--leather-tan) 70%);
  }
  .offer-band {
    position: absolute;
    left: 22px;
    width: 1162px;
    height: 109px;
    background: var(--ink);
    box-shadow: 0 2px 4px var(--shadow);
    display: flex;
    align-items: center;
    justify-content: center;
    font-weight: 300;
    white-space: nowrap;
  }
  .offer-band.discount { top: 484px; font-size: 45px; }
  .offer-band.shipping { top: 621px; font-size: 36px; }
  .offer-band.monogram { top: 758px; font-size: 36px; }
  .offer-band em { font-style: italic; font-size: 28px; }
</style>
</head>
<body>
<main class="newsletter">
  <header class="occasion-bar">
    <svg width="1162" height="70" viewBox="0 0 1162 70" aria-hidden="true">
      <polygon points="0,0 168,0 286,70 0,70" fill="var(--ink)"/>
      <polygon points="248,0 1162,0 1162,70 368,70" fill="var(--ink)"/>
    </svg>
    <span class="occasion-label graduation">Graduation Gift</span>
    <span class="occasion-label fathers-day">Father’s Day</span>
    <span class="occasion-year">2015</span>
  </header>

  <section class="product-stage">
    <svg width="1162" height="332" viewBox="0 0 1162 332" aria-hidden="true">
      <polygon points="0,0 333,0 618,167 333,332 0,332" fill="var(--paper)"/>
      <polygon points="410,0 1162,0 1162,332 410,332 692,167" fill="var(--paper)"/>
    </svg>
    <div class="product-photo backpack" role="img" aria-label="Glossy reddish-brown leather backpack with buckled front pockets"></div>
    <div class="product-photo briefcase" role="img" aria-label="Brown leather briefcase with shoulder strap and front clasp"></div>
  </section>

  <p class="offer-band discount">40% - 75% Off Storewide!</p>
  <p class="offer-band shipping">Free Shipping On All Orders&nbsp;<span>(<em>No Minimum Required</em>)!</span></p>
  <p class="offer-band monogram">Make it extra special with a custom monogram!</p>
</main>
</body>
</html>
```